Velsori Biotechnology needs a professional powerpoint design

We would like to re-design our powerpoint template(as attachment 1), it should be based on our current logo (as attachment 2). We hope the new powerpoint template could be more professional and like a biotechnology company with advanced technology.
Velsori Biotechnology is a contract development and manufacturing organization to provide high quality services to our clients in development, lead-in advanced technology and cGMP manufacturing of biopharmaceuticals from clinical to commercial manufacturing. We offers the advanced technology and services to become the best partner for clients from clinical to commercial manufacturing.
Reason: We would like to extend the deadline for this project so that designers can have more time to prepare, thanks.
Target Market(s)
Velsori Biotechnology is a contract development and manufacturing organization to provide high quality services to our clients in development, lead-in advanced technology and cGMP manufacturing of biopharmaceuticals from clinical to commercial manufacturing.
Velsori primary focus on development and manufacturing of glycoprotein pharmaceuticals against breast cancer, supplies KEP Taiwan with KEP-437 & KEP-438 for global clinical trials and commercialization in the future. Velsori offers the advanced technology and services to become the best partner for clients from clinical to commercial manufacturing.
Industry/Entity Type
Biotechnology
Requirements
Must have
- The new powerpoint design should based on our current logo.
Should not have
- The similar design with current powerpoint style. Please don't refer the design style of our current website http://www.velsori-example.com.tw/ as well, we will re-design it soon.

```html
<!DOCTYPE html>
<html lang="en">
<head>
<meta charset="utf-8">
<title>Velsori Biotechnology – Presentation Template</title>
<link rel="stylesheet" href="https://fonts.googleapis.com/css2?family=Nunito:wght@300;400;700;800&display=swap">
<style>
  :root {
    --stage: #333333;
    --slide-white: #ffffff;
    --deep-blue: #2a54a8;
    --mid-blue: #3a73c4;
    --teal: #2fa3a8;
    --band-blue: #1f66b8;
    --band-light: #3d9ad8;
    --ink: #111111;
    --body-ink: #555555;
    --list-ink: #666666;
    --brand-ink: #0f3a2a;
    --brand-dot: #3f8c3a;
  }
  * { box-sizing: border-box; margin: 0; padding: 0; }
  html, body { width: 771px; height: 1200px; overflow: hidden; }
  body {
    background: var(--stage);
    font-family: "Nunito", sans-serif;
    position: relative;
  }
  .slide {
    position: absolute;
    left: 193px;
    width: 417px;
    height: 243px;
    overflow: hidden;
  }
  .slide--cover { top: 65px; width: 401px; }
  .slide--about { top: 342px; }
  .slide--services { top: 625px; }
  .slide--closing { top: 914px; }

  .slide--blue {
    background: radial-gradient(ellipse at 35% 30%, var(--mid-blue) 0%, var(--deep-blue) 75%);
  }
  .leaf-field {
    position: absolute;
    right: 0; top: 0;
    width: 62%; height: 100%;
    background: radial-gradient(ellipse at 60% 55%, rgba(47,163,168,0.75) 0%, rgba(47,163,168,0.35) 45%, rgba(47,163,168,0) 75%);
  }

  .brand {
    position: absolute;
    display: flex;
    align-items: center;
    gap: 6px;
    font-weight: 800;
    color: var(--brand-ink);
  }
  .brand__dot {
    width: 14px; height: 14px;
    border-radius: 50%;
    background: var(--brand-dot);
  }
  .slide--cover .brand { left: 34px; top: 180px; font-size: 22px; letter-spacing: 1px; }
  .slide--cover .brand__dot { width: 22px; height: 22px; }

  .slide--white { background: var(--slide-white); }
  .slide__title {
    position: absolute;
    left: 21px; top: 20px;
    font-size: 20px;
    font-weight: 700;
    color: var(--ink);
  }
  .about__body {
    position: absolute;
    left: 24px; top: 62px;
    width: 370px;
    font-size: 5.6px;
    line-height: 8.6px;
    font-weight: 300;
    color: var(--body-ink);
    text-align: justify;
  }
  .about__body p + p { margin-top: 8px; }

  .services__lead {
    position: absolute;
    left: 24px; top: 62px;
    font-size: 11px;
    font-weight: 300;
    color: var(--list-ink);
  }
  .services__list {
    position: absolute;
    left: 24px; top: 88px;
    list-style: none;
    font-size: 9.5px;
    line-height: 11.6px;
    font-weight: 300;
    color: var(--list-ink);
  }
  .services__list li::before {
    content: "•";
    display: inline-block;
    width: 13px;
  }

  .slide--white .brand {
    right: 14px; bottom: 22px;
    font-size: 9px;
  }
  .footer-band {
    position: absolute;
    left: 0; bottom: 0;
    width: 100%; height: 14px;
  }

  .contact {
    position: absolute;
    left: 0; right: 0; top: 203px;
    text-align: center;
    color: #ffffff;
    font-size: 5.4px;
    line-height: 8.4px;
    font-weight: 400;
    transform: translateX(34px);
  }
  .contact__name { font-size: 7.6px; font-weight: 700; line-height: 10px; }
</style>
</head>
<body>

  <section class="slide slide--blue slide--cover">
    <div class="leaf-field" role="img" aria-label="Soft field of translucent teal leaves rising on the right"></div>
    <div class="brand"><span class="brand__dot"></span>Velsori Biotech</div>
  </section>

  <section class="slide slide--white slide--about">
    <h2 class="slide__title">Who We Are</h2>
    <div class="about__body">
      <p>Velsori Biotechnology is a contract development and manufacturing partner specializing in glycoprotein biopharmaceuticals. From cell line development to process design and cGMP production, our scientists and engineers guide every program with care. We work with partners worldwide, providing clients with reliable, scalable and well documented solutions using today's most advanced technology. Velsori is committed to excellence.</p>
      <p>Our quality team is a dedicated group within Velsori providing analytical and release services, including stability studies, method validation, bioassays and impurity testing. We support programs of all sizes, clinical and commercial. Our facility in Taiwan is licensed for the manufacture, testing and release of biologic drug products.</p>
    </div>
    <div class="brand"><span class="brand__dot"></span>Velsori</div>
    <svg class="footer-band" viewBox="0 0 417 14" preserveAspectRatio="none" aria-hidden="true">
      <rect x="0" y="9" width="417" height="5" fill="var(--band-blue)"/>
      <polygon points="350,4 417,4 417,14 340,14" fill="var(--band-light)"/>
    </svg>
  </section>

  <section class="slide slide--white slide--services">
    <h2 class="slide__title">Services &amp; Solutions</h2>
    <p class="services__lead">We offer:</p>
    <ul class="services__list">
      <li>Structured Cabling</li>
      <li>Electronic Security and Surveillance</li>
      <li>Fire</li>
      <li>In-Building Wireless</li>
      <li>Sound Masking</li>
      <li>Monitoring</li>
      <li>National Rollout Support</li>
    </ul>
    <div class="brand"><span class="brand__dot"></span>Velsori</div>
    <svg class="footer-band" viewBox="0 0 417 14" preserveAspectRatio="none" aria-hidden="true">
      <rect x="0" y="9" width="417" height="5" fill="var(--band-blue)"/>
      <polygon points="350,4 417,4 417,14 340,14" fill="var(--band-light)"/>
    </svg>
  </section>

  <section class="slide slide--blue slide--closing">
    <div class="leaf-field" role="img" aria-label="Soft field of translucent teal leaves rising on the right"></div>
    <div class="contact">
      <p class="contact__name">VELSORI BIOTECH</p>
      <p>012.345.6789</p>
      <p>INFO@VELSORI-EXAMPLE.COM</p>
      <p>WWW.VELSORI-EXAMPLE.COM</p>
    </div>
  </section>

</body>
</html>
```